Small soho-London based IT Support company website

We've had our logo and stationary redesigned on Sketch Harbor and now we'd like our website done.
We're a small IT support company. Our client base is mainly design studios and advertising agencies working mainly on Zobs.
As such our website needs to be young clean and professional looking.
Our current site can be viewed at http://orvane-lux.it
We currently use Joomla but we're happy to move to Wordpress if that's the only option.

```html
<!DOCTYPE html>
<html lang="en">
<head>
<meta charset="utf-8">
<title>Brisk Technical Services</title>
<link href="https://fonts.googleapis.com/css2?family=Questrial&family=Open+Sans:wght@400;600&display=swap" rel="stylesheet">
<style>
:root{
  --page:#ffffff;
  --band:#1c2025;
  --band-2:#2a3038;
  --lime:#b9d22a;
  --lime-dark:#8fa81a;
  --sky:#5ba3c9;
  --ink:#333333;
  --ink-soft:#555555;
  --muted:#999999;
  --rule:#e4e4e4;
  --footer-text:#6d737a;
}
*{margin:0;padding:0;box-sizing:border-box}
html,body{width:1000px;height:1200px;overflow:hidden;background:var(--page)}
body{position:relative;font-family:"Open Sans",Arial,sans-serif;color:var(--ink)}
.abs{position:absolute}
.head-band{left:107px;top:0;width:786px;height:268px;background:radial-gradient(ellipse at 50% 30%,var(--band-2),var(--band) 70%)}
.foot-band{left:107px;top:1075px;width:786px;height:125px;background:linear-gradient(var(--band-2),var(--band))}
.brand{left:222px;top:14px;display:flex;align-items:center;gap:8px;font-family:"Questrial",sans-serif;font-size:34px;color:var(--lime)}
.brand-dot{width:12px;height:12px;border-radius:50%;background:var(--lime)}
.topline{top:9px;font-size:8px;color:var(--lime);display:flex;align-items:center;gap:5px;letter-spacing:.3px}
.nav{top:40px;left:491px;display:flex;gap:0;font-size:8px;color:#aab0b6;text-transform:uppercase}
.nav span{display:block;padding:0 6px 16px;margin-right:8px}
.nav .active{color:#fff;border-bottom:3px solid #cfd3d6}
.head-rule{left:212px;top:67px;width:576px;height:1px;background:#363c44}
.welcome{left:107px;top:88px;width:786px;text-align:center;font-family:"Questrial",sans-serif;font-size:28px;color:#fff}
.welcome em{font-style:normal;color:var(--lime)}
.panel{left:212px;top:145px;width:576px;height:930px;background:var(--page)}
.hero{left:224px;top:157px;width:552px;height:222px;background:linear-gradient(100deg,#c9a57a 0%,#8a7566 28%,#8fb0c8 45%,#3d7ec4 65%,#2f6fbe 100%)}
.hello{left:224px;top:385px;font-family:"Questrial",sans-serif;font-size:22px;color:var(--ink)}
.intro{left:224px;top:419px;width:560px;font-size:9.5px;line-height:11px;color:var(--muted)}
.intro p+p{margin-top:12px}
.divider{left:224px;width:552px;height:3px;background:#eeeeee}
.col{top:500px;width:125px}
.col h2{display:flex;align-items:center;gap:8px;font-family:"Questrial",sans-serif;font-weight:400;font-size:19px;color:var(--ink);height:26px}
.col p,.col li{font-size:7.6px;line-height:13px;color:var(--ink-soft)}
.col .body{margin-top:9px}
.col p+p,.col p+ul{margin-top:13px}
.col ul{list-style:none}
.col li:before{content:"• "}
.tablet{left:637px;top:537px;width:139px;height:178px;border-radius:10px;background:#151515;box-shadow:0 4px 6px rgba(0,0,0,.15)}
.screen{position:absolute;left:15px;top:14px;width:109px;height:146px;background:#fff;padding:10px 8px 0 8px;font-size:7.3px;color:#444}
.row{display:flex;justify-content:space-between;align-items:center;height:18px}
.spin{width:32px;height:11px;border:1px solid #bbb;font-size:7px;padding-left:3px;line-height:9px}
.check{display:flex;align-items:center;gap:5px;height:14px}
.check i{width:8px;height:8px;border:1px solid #999;display:block}
.estimate{margin-top:7px;border:1px solid #ddd;height:14px;line-height:12px;padding-left:4px;color:#777}
.learn{margin-top:14px;height:11px;border-radius:6px;background:linear-gradient(#777,#444);color:#fff;text-align:center;line-height:11px;font-size:6.5px}
.home-btn{position:absolute;left:64px;top:166px;width:10px;height:4px;border-radius:2px;background:#333}
.sect-title{top:760px;font-size:10.5px;font-weight:600;color:var(--ink)}
.svc-list{left:230px;top:783px;width:117px;list-style:none}
.svc-list li{height:21.2px;display:flex;align-items:center;gap:6px;font-size:7.6px;color:var(--ink-soft);border-bottom:1px solid var(--rule);padding-left:2px}
.loc-text{left:362px;top:785px;width:415px;font-size:7.6px;line-height:13px;color:var(--ink-soft)}
.postcode{left:362px;top:823px;display:flex;align-items:center;gap:8px;font-size:7.6px;color:var(--ink-soft)}
.postcode .field{width:43px;height:13px;border:1px solid #ccc;font-size:7px;line-height:11px;text-align:center;color:#335}
.postcode .go{width:26px;height:13px;border:1px solid #aaa;border-radius:4px;background:linear-gradient(#fafafa,#ddd);font-size:7px;line-height:11px;text-align:center;color:#333}
.map{left:363px;top:851px;width:413px;height:194px;background:linear-gradient(135deg,#ebe6da,#e2dccb 60%,#efe9d9);border:1px solid #ddd}
.foot-label{left:213px;top:1086px;font-size:7px;color:var(--sky);text-transform:uppercase}
.foot-col{top:1103px;list-style:none;font-size:7.4px;line-height:13px;color:var(--footer-text)}
.subscribe{left:620px;top:1086px;width:168px;height:74px;border-radius:4px;background:#111418;padding:6px 0 0 9px;font-family:"Questrial",sans-serif}
.subscribe .s1{font-size:18px;line-height:17px;color:#fff;letter-spacing:.5px}
.subscribe .s2{font-size:12px;line-height:12px;color:var(--sky)}
.subscribe .field{position:absolute;left:10px;top:44px;width:97px;height:22px;background:#050607;border:1px solid #2a2e33}
.subscribe .btn{position:absolute;left:107px;top:44px;width:48px;height:22px;background:#22272d;color:var(--lime);font-size:12px;line-height:22px;text-align:center}
.foot-rule{left:213px;top:1176px;width:575px;height:1px;background:#30363d}
.follow{left:213px;top:1185px;font-size:6.5px;color:var(--footer-text);display:flex;align-items:center;gap:4px}
.follow b{display:block;width:9px;height:9px;background:#3a6ea8}
.copy{right:212px;top:1187px;font-size:6.5px;color:var(--footer-text)}
</style>
</head>
<body>
<div class="abs head-band"></div>
<div class="abs foot-band"></div>

<header>
  <div class="abs brand"><span>Brisk Tech</span><span class="brand-dot"></span></div>
  <div class="abs topline" style="left:626px">
    <svg width="9" height="9" viewBox="0 0 10 10"><path d="M2 1l2 2-1 1.5a6 6 0 0 0 2.5 2.5L7 6l2 2-1.2 1.5C4.5 9.5.5 5.5.5 2.2z" fill="#9aa0a6"/></svg>
    PHONE : 0203 555 0147
  </div>
  <div class="abs topline" style="left:733px">
    <svg width="10" height="8" viewBox="0 0 10 8"><rect x=".5" y=".5" width="9" height="7" fill="#9aa0a6"/><path d="M.5.5L5 4.5 9.5.5" stroke="#1c2025" fill="none"/></svg>
    EMAIL US
  </div>
  <nav class="abs nav">
    <span class="active">Home</span><span>About Us</span><span>Services</span><span>Why Us</span><span>Contact</span>
  </nav>
  <div class="abs head-rule"></div>
  <h1 class="abs welcome" style="font-weight:400">Welcome to <em>Brisk</em> Technical Services</h1>
</header>

<main>
  <div class="abs panel"></div>
  <div class="abs hero" role="img" aria-label="Photo of two professionals looking at transparent screens showing data and a globe"></div>

  <h2 class="abs hello" style="font-weight:400">Hello,</h2>
  <div class="abs intro">
    <p>We're Brisk. Located in Soho - London, trusted by small medium and large companies to provide quick effective responses to their technical needs.</p>
    <p>We are the West End's outsourced IT department</p>
  </div>
  <div class="abs divider" style="top:480px"></div>

  <section class="abs col" style="left:224px">
    <h2><svg width="26" height="24" viewBox="0 0 26 24"><rect x="1" y="1" width="24" height="17" rx="1" fill="#444"/><rect x="3" y="3" width="20" height="13" fill="#3a7fd0"/><rect x="9" y="18" width="8" height="4" fill="#999"/></svg>Zob</h2>
    <div class="body">
      <p>We have over 50 combined years in supporting Zob systems.</p>
      <p>Our Pomelo specialists speak plain English so you're not left baffled by computer jargon.</p>
      <ul><li>SME &amp; Corporate Networks</li><li>Velio Email Server</li><li>Bespoke Applications</li><li>Web Services</li><li>Connectivity</li><li>Security</li></ul>
    </div>
  </section>

  <section class="abs col" style="left:362px">
    <h2><svg width="30" height="24" viewBox="0 0 30 24"><rect x="1" y="2" width="20" height="15" fill="#ccc"/><rect x="3" y="4" width="16" height="11" fill="#4b8ad6"/><rect x="22" y="2" width="7" height="20" fill="#bbb"/><rect x="6" y="18" width="10" height="3" fill="#aaa"/></svg>PC</h2>
    <div class="body">
      <p>Friendly Northwind techs with years of industry experience.</p>
      <ul style="margin-top:13px"><li>Northwind Server OS</li><li>PC &amp; Laptop Applications</li><li>Hardware Upgrades</li><li>Antivirus &amp; Spam</li><li>Firewall Security</li><li>Email Filtering</li><li>Networking</li><li>Backups</li><li>Security</li></ul>
    </div>
  </section>

  <section class="abs col" style="left:503px">
    <h2><svg width="30" height="24" viewBox="0 0 30 24"><rect x="2" y="1" width="22" height="15" fill="#444"/><rect x="4" y="3" width="18" height="11" fill="#4b8ad6"/><rect x="0" y="17" width="26" height="4" fill="#999"/><circle cx="26" cy="18" r="4" fill="#333"/></svg>Combined</h2>
    <div class="body">
      <p>Using both Zobs &amp; PC's can be tricky but not with us.</p>
      <p>Brisk is a joint venture between two IT directors, one Zob focused and one PC focused but both with proven track records in running successful IT supports firms.</p>
      <p>Our engineers are specialists not all rounders. This means you get the correct fix not a hack.</p>
    </div>
  </section>

  <section class="abs col" style="left:639px;width:140px">
    <h2><svg width="28" height="24" viewBox="0 0 28 24"><rect x="1" y="2" width="26" height="16" rx="4" fill="#e6e6e6" stroke="#ccc"/><path d="M8 18l-2 5 6-5z" fill="#e6e6e6"/></svg>Insti-Quote</h2>
  </section>
  <div class="abs tablet">
    <div class="screen">
      <div class="row">Laptops <span class="spin">0</span></div>
      <div class="row">Desktops <span class="spin">0</span></div>
      <div class="row">Servers <span class="spin">0</span></div>
      <div class="check" style="margin-top:4px"><i></i>Remote Support</div>
      <div class="check"><i></i>Server Monitoring</div>
      <div class="estimate">Monthly Estimate</div>
      <div class="learn">Learn More</div>
    </div>
    <span class="home-btn"></span>
  </div>

  <div class="abs divider" style="top:742px"></div>

  <h3 class="abs sect-title" style="left:225px">Our Services</h3>
  <ul class="abs svc-list">
    <li><svg width="5" height="6" viewBox="0 0 5 6"><path d="M0 0l5 3-5 3z" fill="#bbb"/></svg>Regular Maintenance</li>
    <li><svg width="5" height="6" viewBox="0 0 5 6"><path d="M0 0l5 3-5 3z" fill="#bbb"/></svg>Monitoring</li>
    <li><svg width="5" height="6" viewBox="0 0 5 6"><path d="M0 0l5 3-5 3z" fill="#bbb"/></svg>Remote Support</li>
    <li><svg width="5" height="6" viewBox="0 0 5 6"><path d="M0 0l5 3-5 3z" fill="#bbb"/></svg>Emergency Support</li>
    <li><svg width="5" height="6" viewBox="0 0 5 6"><path d="M0 0l5 3-5 3z" fill="#bbb"/></svg>IT Manager</li>
    <li><svg width="5" height="6" viewBox="0 0 5 6"><path d="M0 0l5 3-5 3z" fill="#bbb"/></svg>IT Roadmap</li>
    <li><svg width="5" height="6" viewBox="0 0 5 6"><path d="M0 0l5 3-5 3z" fill="#bbb"/></svg>Asset Management</li>
    <li><svg width="5" height="6" viewBox="0 0 5 6"><path d="M0 0l5 3-5 3z" fill="#bbb"/></svg>Online Backup</li>
    <li><svg width="5" height="6" viewBox="0 0 5 6"><path d="M0 0l5 3-5 3z" fill="#bbb"/></svg>Tape pickup</li>
    <li><svg width="5" height="6" viewBox="0 0 5 6"><path d="M0 0l5 3-5 3z" fill="#bbb"/></svg>Email Spam &amp; Virus filtering</li>
    <li><svg width="5" height="6" viewBox="0 0 5 6"><path d="M0 0l5 3-5 3z" fill="#bbb"/></svg>Network Virus protection</li>
    <li><svg width="5" height="6" viewBox="0 0 5 6"><path d="M0 0l5 3-5 3z" fill="#bbb"/></svg>Night Work</li>
  </ul>

  <h3 class="abs sect-title" style="left:362px">Location</h3>
  <p class="abs loc-text">This map shows where we are, smack bang in the middle of Soho and Covent Garden. Type your postcode in to see how close we are to your offices.</p>
  <div class="abs postcode">Enter your postcode: <span class="field">W1X 9QZ</span><span class="go">GO</span></div>
  <div class="abs map" role="img" aria-label="Street map of Soho and Covent Garden with the office location marked"></div>
</main>

<footer>
  <div class="abs foot-label">Our Services</div>
  <ul class="abs foot-col" style="left:213px"><li>Regular Maintenance</li><li>Monitoring</li><li>Remote Support</li><li>Emergency Support</li></ul>
  <ul class="abs foot-col" style="left:325px;top:1107px"><li>IT Manager</li><li>IT Roadmap</li><li>Asset Management</li><li>Online Backup</li></ul>
  <ul class="abs foot-col" style="left:423px;top:1107px"><li>Tape pickup</li><li>Email Spam &amp; Virus filtering</li><li>Network Virus protection</li><li>Night Work</li></ul>
  <div class="abs subscribe">
    <div class="s1">SUBSCRIBE</div>
    <div class="s2">TO OUR NEWSLETTER</div>
    <div class="field"></div>
    <div class="btn">Sign Up</div>
  </div>
  <div class="abs foot-rule"></div>
  <div class="abs follow">FOLLOW US ON: <b style="margin-left:4px"></b><b style="background:#4aa3df"></b><b style="background:#2a6496"></b></div>
  <div class="abs copy">© BRISK TECH LTD 2011</div>
</footer>
</body>
</html>
```